Flyer für ambulante und teilstationäre Pflege
Zielgruppe
ambulante und teilstationäre Pflege
Zielgruppe: Pflegebedürftige Menschen, die noch ausreichend mobil sind, um als Gast in unserer Tagespflege zu sein
Aufgabenstellung
Standard DIN lang Format
Stil soll unserer Homepage folgen: www.pflegeteam-sonnhalde.de
Wir achten immer sehr darauf, nicht so einen verstaubten Stil wie viele andere Pflegeeinrichtungen zu haben, sondern fröhlich, bunt , ansprechend

```html
<!DOCTYPE html>
<html lang="de">
<head>
<meta charset="utf-8">
<title>Flyer Pflegeteam Sonnhalde</title>
<link href="https://fonts.googleapis.com/css2?family=Poppins:ital,wght@0,400;0,500;0,600;0,700;1,600&display=swap" rel="stylesheet">
<style>
:root{
  --teal:#2d9a8e;
  --teal-band:#33928a;
  --red:#9b1c24;
  --pink:#d6b6c6;
  --pink-strip:#dcbccb;
  --grey-band:#dcdcdc;
  --ink:#1d1d1d;
  --muted:#6b6b6b;
  --stage:#a9a9a9;
  --white:#ffffff;
}
*{margin:0;padding:0;box-sizing:border-box}
html,body{width:1200px;height:1117px;overflow:hidden}
body{background:var(--stage);font-family:'Poppins',sans-serif;color:var(--ink);position:relative}
.page{position:absolute;top:184px;width:531px;height:750px;background:var(--white);overflow:hidden}
.page--front{left:58px}
.page--back{left:610px}
.abs{position:absolute}
.strip{left:0;width:100%;height:7px;background:var(--pink-strip)}

/* front */
.brand-row{left:0;top:22px;width:100%;display:flex;justify-content:center;align-items:center;gap:12px}
.brand{display:flex;align-items:center;gap:7px;font-weight:500;color:var(--muted);font-size:10px;letter-spacing:.2px;white-space:nowrap}
.brand__dot{width:30px;height:30px;border-radius:50%;flex:none}
.brand--day .brand__dot{background:var(--teal)}
.brand--care .brand__dot{background:var(--red)}
.brand-divider{width:1px;height:40px;background:#cfcfcf;flex:none}
.headline{left:0;top:84px;width:100%;text-align:center;color:var(--teal);font-weight:700;font-size:30px;line-height:31px}
.welcome{left:0;top:153px;width:100%;text-align:center;font-weight:600;font-size:10px}
.photo{background:linear-gradient(120deg,#d9b89c,#ece4dc 55%,#c9d6c8)}
.photo--hero{left:0;top:180px;width:531px;height:169px}
.intro{left:45px;top:363px;width:441px;text-align:center;font-size:9.5px;line-height:12.3px}
.intro p+p{margin-top:12px}
.features{left:0;top:450px;width:254px;height:238px;background:var(--red);color:var(--white)}
.features__title{position:absolute;right:20px;top:14px;text-align:right;font-weight:700;font-size:14.5px;line-height:16px}
.feature{position:absolute;display:flex;align-items:center;gap:12px;font-size:10.3px;line-height:11.8px}
.feature svg{flex:none}
.photo--care{left:254px;top:461px;width:263px;height:240px;background:linear-gradient(135deg,#cfc6d6,#7c5a74 55%,#e9e3e1)}
.url-band{left:0;top:671px;width:100%;height:79px;background:var(--teal-band)}
.url{left:0;top:712px;width:100%;text-align:center;color:var(--white);font-weight:700;font-size:15px}

/* back */
.back-title{left:0;top:0;width:256px;height:104px;background:var(--red);color:var(--white);font-weight:700;font-size:20px;line-height:22.5px;padding:20px 0 0 35px}
.photo--cake{left:266px;top:0;width:265px;height:128px;background:linear-gradient(135deg,#b79a6c,#f0e7d2 50%,#8a6a44)}
.grey-band{left:0;top:283px;width:100%;height:219px;background:var(--grey-band)}
.lead{left:35px;top:116px;width:220px;color:var(--teal);font-weight:700;font-size:14px;line-height:15.8px}
.photo--group{left:25px;top:227px;width:260px;height:263px;background:linear-gradient(160deg,#9fb0c8,#6d7a5c 60%,#4f6a34)}
.textbox{left:266px;top:139px;width:242px;height:336px;background:var(--white);box-shadow:2px 3px 6px rgba(0,0,0,.25);padding:14px 18px 0 20px;font-size:8.6px;line-height:11px}
.textbox p+p{margin-top:11px}
.quote-band{left:0;top:502px;width:100%;height:109px;background:var(--pink)}
.quote{left:35px;top:527px;width:463px;height:58px;border:2px solid var(--white);border-radius:6px;color:var(--white);font-style:italic;font-weight:600;font-size:9px;line-height:12px;text-align:center;padding:8px 20px 0}
.quote__author{left:210px;top:578px;width:110px;background:var(--pink);text-align:center;color:var(--white);font-style:italic;font-weight:700;font-size:11.5px}
.cta{left:0;top:611px;width:100%;height:53px;background:var(--teal-band);color:var(--white);font-weight:600;font-size:10.2px;line-height:12.6px;text-align:center;padding-top:13px}
.contact{font-size:10px;line-height:16.5px}
.contact--left{left:47px;top:679px}
.contact--right{left:262px;top:677px;line-height:12px}
.contact li{list-style:none;display:flex;align-items:flex-start;gap:7px}
.contact--right li+li{margin-top:10px}
.contact svg{flex:none;margin-top:3px}
</style>
</head>
<body>

<section class="page page--front">
  <div class="abs strip" style="top:0"></div>
  <div class="abs brand-row">
    <div class="brand brand--day"><span>TAGESPFLEGE AM LINDENHOF</span><span class="brand__dot"></span></div>
    <div class="brand-divider"></div>
    <div class="brand brand--care"><span>PFLEGETEAM SONNHALDE</span><span class="brand__dot"></span></div>
  </div>

  <h1 class="abs headline">Von Mensch zu Mensch -<br>Pflegeprofis seit 1994</h1>
  <p class="abs welcome">Herzlich Willkommen bei der Pflegeteam Sonnhalde &amp; Lindenau</p>

  <div class="abs photo photo--hero" role="img" aria-label="Foto: junge Pflegerin legt lächelnd den Arm um eine ältere Dame mit Brille"></div>

  <div class="abs intro">
    <p>Seit fast 30 Jahren sind wir nun schon Ihr Experte für häusliche Pflege und Demenzbetreuung. Ihr persönliches Wohl und das Ihrer Angehörigen liegt uns am Herzen,</p>
    <p>Lassen Sie sich von uns in Ihrem Alltag behilflich sein und machen Sie noch heute einen Beratungstermin zu unseren Dienstleistungen mit einem unserer kompetenten Ansprechpartner.</p>
  </div>

  <div class="abs url-band"></div>
  <div class="abs photo photo--care" role="img" aria-label="Foto: Pfleger und ältere Dame hören lachend gemeinsam Musik mit Kopfhörern"></div>

  <div class="abs features">
    <h2 class="features__title">Was unseren Pflegedienst<br>auszeichnet</h2>
    <div class="feature" style="top:48px;left:17px">
      <svg width="38" height="38" viewBox="0 0 38 38"><circle cx="19" cy="19" r="17" fill="none" stroke="#fff" stroke-width="2"/><circle cx="19" cy="16" r="3" fill="#fff"/><circle cx="12.5" cy="18" r="2.4" fill="#fff"/><circle cx="25.5" cy="18" r="2.4" fill="#fff"/><path d="M13 27a6 6 0 0 1 12 0z" fill="#fff"/></svg>
      <span>Über 25 Jahre Erfahrung</span>
    </div>
    <div class="feature" style="top:90px;left:17px">
      <svg width="38" height="38" viewBox="0 0 38 38"><circle cx="19" cy="19" r="17" fill="none" stroke="#fff" stroke-width="2"/><rect x="13" y="10" width="12" height="17" rx="1" fill="#fff"/><path d="M15.5 15h7M15.5 18.5h7M15.5 22h5" stroke="#9b1c24" stroke-width="1.3"/></svg>
      <span>Abgestimmtes<br>Versorgungskonzept mit<br>Beratung zur Finanzierung</span>
    </div>
    <div class="feature" style="top:136px;left:17px">
      <svg width="38" height="38" viewBox="0 0 38 38"><circle cx="19" cy="19" r="17" fill="none" stroke="#fff" stroke-width="2"/><circle cx="19" cy="16" r="6" fill="none" stroke="#fff" stroke-width="2"/><path d="M15 21l-3 7 4-1 2 3 1-6M23 21l3 7-4-1-2 3-1-6" fill="#fff"/></svg>
      <span>Sehr gute MDK geprüfte<br>Pflegequalität auf höchstem<br>Niveau</span>
    </div>
    <div class="feature" style="top:183px;left:17px">
      <svg width="38" height="38" viewBox="0 0 38 38"><circle cx="19" cy="19" r="17" fill="none" stroke="#fff" stroke-width="2"/><rect x="14" y="10" width="12" height="16" rx="1" fill="#fff"/><circle cx="15" cy="25" r="4.5" fill="#9b1c24" stroke="#fff" stroke-width="1.5"/><path d="M13 25l1.5 1.5 3-3" stroke="#fff" stroke-width="1.3" fill="none"/></svg>
      <span>Zulassung und<br>Versorgungsvertrag mit allen<br>Kranken- und Pflegekassen</span>
    </div>
  </div>

  <p class="abs url">www.pflegeteam-sonnhalde.de</p>
</section>

<section class="page page--back">
  <div class="abs grey-band"></div>
  <h2 class="abs back-title">Abwechslungsreiche<br>Beschäftigung in der<br>Tagespflege</h2>
  <div class="abs photo photo--cake" role="img" aria-label="Foto: Platte mit Sahnetörtchen und Erdbeeren"></div>

  <p class="abs lead">Besonders für Demenzkranke ist unsere stimulierende Tagespflege nicht einfach nur zweckmäßig, sondern spricht die Sinne an und lädt zum Verweilen ein.</p>

  <div class="abs photo photo--group" role="img" aria-label="Foto: vier Tagesgäste und Betreuerin sitzen gemeinsam auf einer Bank im Freien"></div>

  <div class="abs textbox">
    <p>Seit dem 15.01.2019 besitzen wir eine teilstationäre Tagespflegeeinrichtung mit 16 Plätzen im Gesundheitszentrum Lindenau. So können wir Ihnen auf einer Fläche von 243 m² mit Sonnenterrasse in gemütlicher Atmosphäre noch mehr Unterstützung anbieten.</p>
    <p>Bei uns können Sie sich auf eine abwechslungsreiche Betreuung und Beschäftigung an 5 Tagen der Woche freuen, die stets am Bedarf und den Vorlieben unserer Tagesgäste orientiert ist.</p>
    <p>Während Ihres Aufenthalts erhalten Sie professionelle medizinische und pflegerische Versorgung.</p>
    <p>In netter Gesellschaft können Sie soziale Kontakte knüpfen oder aufrechterhalten. Falls Sie doch einmal Ruhe benötigen, gibt es selbstverständlich Rückzugsmöglichkeiten.</p>
    <p>Nach Bedarf bieten wir Frühstück, selbst gekochtes Mittagessen, Nachmittagskaffee sowie Softgetränke an. Sie können selbst an- und abreisen oder alternativ können wir Sie abholen und nach Hause bringen.</p>
  </div>

  <div class="abs quote-band"></div>
  <blockquote class="abs quote">"Ich habe eine Tagespflege gesucht und die neu errichtete Einrichtung von der Sonnhalde GmbH in Lindenau ist echt super. Das Gebäude ist neu, das Personal super und alles klappt bisher echt gut, kann ich nur empfehlen."</blockquote>
  <p class="abs quote__author">-Frau M</p>

  <p class="abs cta">Nirgends sonst in der Region erhalten Sie so hochqualitative und zuverlässige Pflege<br>wie bei uns! Wir helfen Ihnen dabei, Ihr Leben einfacher zu gestalten. Rufen Sie uns an!</p>

  <ul class="abs contact contact--left">
    <li><svg width="10" height="10" viewBox="0 0 10 10"><circle cx="5" cy="5" r="5" fill="#9b1c24"/><path d="M3.3 2.6l1 1-.5.7a3 3 0 0 0 1.9 1.9l.7-.5 1 1-.6.8A4.5 4.5 0 0 1 2.5 3.2z" fill="#fff"/></svg>Sonnhalde: +49(0) 4300 12 34</li>
    <li><svg width="10" height="10" viewBox="0 0 10 10"><circle cx="5" cy="5" r="5" fill="#9b1c24"/><path d="M3.3 2.6l1 1-.5.7a3 3 0 0 0 1.9 1.9l.7-.5 1 1-.6.8A4.5 4.5 0 0 1 2.5 3.2z" fill="#fff"/></svg>Lindenau: +49(0)430 11 22 33 44</li>
    <li><svg width="10" height="10" viewBox="0 0 10 10"><circle cx="5" cy="5" r="5" fill="#9b1c24"/><rect x="2.5" y="3.3" width="5" height="3.6" fill="none" stroke="#fff" stroke-width=".8"/><path d="M2.5 3.3L5 5.3l2.5-2" fill="none" stroke="#fff" stroke-width=".8"/></svg>info@pflegeteam-sonnhalde.de</li>
  </ul>
  <ul class="abs contact contact--right">
    <li><svg width="8" height="11" viewBox="0 0 8 11"><path d="M4 11S0 6.5 0 4a4 4 0 0 1 8 0c0 2.5-4 7-4 7z" fill="#9b1c24"/><circle cx="4" cy="4" r="1.5" fill="#fff"/></svg>Kirchweg 12, Sonnhalde, 24100, Germany</li>
    <li><svg width="8" height="11" viewBox="0 0 8 11"><path d="M4 11S0 6.5 0 4a4 4 0 0 1 8 0c0 2.5-4 7-4 7z" fill="#9b1c24"/><circle cx="4" cy="4" r="1.5" fill="#fff"/></svg><span>Lindenhof 7, Lindenau,<br>24110, Germany</span></li>
  </ul>

  <div class="abs strip" style="top:743px"></div>
</section>

</body>
</html>
```